Brindle Search Business Card for recruitment company

We are looking for a Business Card Design that incorporates our personal details and our busines name and logo. We are a specialized search consultancy that recruit Property and Construction professionals.
We would like a business card that stands out and is appealing to the Construction and Property industry as well.

Target Market(s)

people in the construction and property industry

Contact Information for Business Card

Business Name and logo

Font styles to use
Serif

Colors
0094D4
00A9DD
6FCCEA
C7EBF8
E9F6FB

Requirements
Must have
• Business name and logo as well as contact details
Should not have
• No photos of us please

```html
<!DOCTYPE html>
<html lang="en">
<head>
<meta charset="utf-8">
<title>Brindle Search – Business Card</title>
<link href="https://fonts.googleapis.com/css2?family=Josefin+Sans:wght@300&family=Arimo:wght@400;700&display=swap" rel="stylesheet">
<style>
  :root {
    --backdrop: #e4e4e2;
    --card-white: #ffffff;
    --ink-navy: #0b4a5e;
    --ink-grey: #555b5f;
    --rule-grey: #8a8a8a;
    --back-teal: #033d50;
    --wordmark-light: #ffffff;
  }
  * { margin: 0; padding: 0; box-sizing: border-box; }
  html, body {
    width: 1200px; height: 801px; overflow: hidden;
    background: var(--backdrop);
  }
  .canvas {
    position: relative; width: 1200px; height: 801px;
    display: flex; align-items: center; justify-content: center; gap: 50px;
  }
  .card {
    position: relative; width: 525px; height: 300px;
    box-shadow: 0 6px 18px rgba(0,0,0,.18);
  }
  .card-front { background: var(--card-white); }
  .card-back { background: var(--back-teal); }

  .wordmark {
    font-family: "Josefin Sans", sans-serif; font-weight: 300;
    letter-spacing: 2px; white-space: nowrap; position: absolute;
  }
  .card-front .wordmark {
    color: var(--ink-navy); font-size: 40px; top: 50px; right: 50px;
  }
  .card-back .wordmark {
    color: var(--wordmark-light); font-size: 36px; right: 40px; bottom: 70px;
  }

  .divider {
    position: absolute; left: 70px; right: 50px; top: 178px;
    height: 1px; background: var(--rule-grey);
  }
  .person {
    position: absolute; left: 48px; bottom: 128px;
    font-family: "Arimo", sans-serif;
  }
  .person-name {
    color: var(--ink-navy); font-weight: 700; font-size: 19px; letter-spacing: .3px;
  }
  .person-title { color: var(--ink-grey); font-size: 14px; margin-top: 2px; }

  .contacts {
    position: absolute; left: 70px; top: 192px; list-style: none;
    font-family: "Arimo", sans-serif; font-size: 14px; color: var(--ink-grey);
    line-height: 21px;
  }
  .contacts li { display: flex; align-items: center; gap: 10px; }
  .contacts svg { width: 12px; height: 12px; flex: none; }

  .address {
    position: absolute; right: 50px; top: 196px; text-align: right;
    font-family: "Arimo", sans-serif; font-size: 14px; line-height: 19px;
    font-style: normal; color: var(--ink-grey);
  }
</style>
</head>
<body>
<main class="canvas">
  <section class="card card-front">
    <div class="wordmark">BRINDLE SEARCH</div>
    <div class="person">
      <div class="person-name">MARCUS HALE</div>
      <div class="person-title">Manager</div>
    </div>
    <div class="divider"></div>
    <ul class="contacts">
      <li>
        <svg viewBox="0 0 12 12" aria-hidden="true"><path d="M3 1 L5 3.5 L4 5 Q5 7 7 8 L8.5 7 L11 9 L9.5 11 Q5 11 2.5 7.5 Q1 5 1.5 2.5 Z" fill="var(--ink-navy)"/></svg>
        555-214-7730
      </li>
      <li>
        <svg viewBox="0 0 12 12" aria-hidden="true"><rect x="1" y="2.5" width="10" height="7" fill="none" stroke="var(--ink-navy)" stroke-width="1.2"/><path d="M1 2.5 L6 6.5 L11 2.5" fill="none" stroke="var(--ink-navy)" stroke-width="1.2"/></svg>
        youremail@mailpost.com
      </li>
      <li>
        <svg viewBox="0 0 12 12" aria-hidden="true"><circle cx="6" cy="6" r="5" fill="none" stroke="var(--ink-navy)" stroke-width="1.1"/><ellipse cx="6" cy="6" rx="2.2" ry="5" fill="none" stroke="var(--ink-navy)" stroke-width="1"/><path d="M1 6 H11 M2 3.5 H10 M2 8.5 H10" stroke="var(--ink-navy)" stroke-width="0.9"/></svg>
        www.brindlesearch.com
      </li>
    </ul>
    <address class="address">Your address, city<br>state, ZIP 0000</address>
  </section>

  <section class="card card-back">
    <div class="wordmark">BRINDLE SEARCH</div>
  </section>
</main>
</body>
</html>
```